Webdesign für Bau von Wohnanlagen aus Containermodulen
Zielgruppe
Wir bauen Wohnanlagen, Bürogebäude, Kindergärten, Schulen etc. aus einzelnen Containermodulen - übernehmen die Montage, Umbau und Versetzung, Reparaturen und Einlagerungen. Unsere Zielgruppe sind überwiegend Firmen und Kommunen. Der Text für die Homepage ist bereits fertig. Hier erhalten Sie weitere Informationen über unser Tätigkeitsfeld.
Aufgabenstellung
Die Farbe unseres Logos ist blau. Sie sollte sich natürlich in der Homepage minimal widerspiegeln, aber nicht dominieren. Bilder sollten nicht zu klein gehalten werden. Wir möchten dadurch zeigen, was möglich ist (z.B. Umsetzungen von ganzen Containeranlagen am Stück - hier haben wir eine Monopolstellung).

```html
<!DOCTYPE html>
<html lang="de">
<head>
<meta charset="utf-8">
<title>Kontakt – Falke Montagearbeiten</title>
<link rel="stylesheet" href="https://fonts.googleapis.com/css2?family=Open+Sans:wght@400;600;700&family=Roboto+Slab:wght@300&display=swap">
<style>
:root{
  --brand:#0c2388;
  --text:#333333;
  --muted:#555555;
  --band:#eeeeee;
  --footer:#5f5f5f;
  --white:#ffffff;
  --map-a:#e4e6d6;
  --map-b:#cfe0b8;
}
*{margin:0;padding:0;box-sizing:border-box}
html,body{width:1200px;height:930px;overflow:hidden;background:var(--white)}
body{font-family:"Open Sans",sans-serif;color:var(--text);position:relative}
.header{position:absolute;left:0;top:0;width:1200px;height:94px}
.brand{position:absolute;left:232px;top:18px;width:170px;height:64px;display:flex;align-items:center;gap:8px;color:var(--brand);font-weight:700;font-size:17px;line-height:1.1;letter-spacing:.5px}
.brand-square{width:14px;height:14px;background:var(--brand);flex:none}
.tagline{position:absolute;left:420px;top:14px;font-family:"Roboto Slab",serif;font-weight:300;font-size:16px;color:var(--muted)}
.nav{position:absolute;top:71px;left:0;width:1200px;height:16px}
.nav a{position:absolute;font-size:10.5px;color:var(--text);text-decoration:none;letter-spacing:.2px;white-space:nowrap}
.nav a.active{color:var(--brand);font-weight:700}
.map{position:absolute;left:0;top:94px;width:1200px;height:308px;background:linear-gradient(110deg,var(--map-b) 0%,var(--map-a) 35%,var(--map-b) 65%,var(--map-a) 100%)}
.crumbs{position:absolute;left:234px;top:411px;font-size:9px;letter-spacing:2px;color:var(--text)}
.crumbs .current{letter-spacing:0;font-size:9.5px;margin-left:4px}
.page-title{position:absolute;left:232px;top:450px;font-size:21px;font-weight:400;color:var(--brand)}
.page-sub{position:absolute;left:232px;top:485px;font-size:12px;font-weight:600;color:var(--brand)}
.intro{position:absolute;left:232px;top:527px;width:740px;font-size:11.4px;line-height:19px;color:var(--text)}
.contact-band{position:absolute;left:0;top:621px;width:1200px;height:271px;background:var(--band)}
.callout{position:absolute;left:232px;top:647px;width:736px;height:50px;background:var(--brand);color:var(--white)}
.callout p{position:absolute;left:15px;top:10px;width:490px;font-size:11.4px;line-height:15px}
.callout .phone{position:absolute;right:13px;top:11px;display:flex;align-items:center;gap:10px;font-size:22px}
.form-title{position:absolute;left:230px;top:719px;font-size:20px;color:var(--brand)}
.address{position:absolute;left:232px;top:752px;font-size:11.6px;line-height:19px;color:var(--text);font-style:normal}
.field{position:absolute;background:var(--white);font-size:11.6px;color:var(--text);padding:2px 11px}
.field.name{left:484px;top:760px;width:232px;height:25px}
.field.mail{left:484px;top:798px;width:232px;height:25px}
.field.tel{left:484px;top:835px;width:232px;height:25px}
.field.msg{left:735px;top:759px;width:233px;height:63px;padding:4px 8px}
.submit{position:absolute;left:860px;top:835px;width:108px;height:25px;background:var(--brand);color:var(--white);font-size:11.6px;font-weight:600;display:flex;align-items:center;justify-content:center}
.footer{position:absolute;left:0;top:892px;width:1200px;height:38px;background:var(--footer);color:var(--white);font-size:9.5px;letter-spacing:2px;padding:17px 0 0 232px;white-space:pre}
</style>
</head>
<body>
<header class="header">
  <div class="brand"><span class="brand-square"></span><span>FALKE<br>MONTAGEARBEITEN</span></div>
  <div class="tagline">Ihr Partner für mobile Container</div>
  <nav class="nav">
    <a style="left:515px">HOME</a>
    <a style="left:571px">LEISTUNGEN</a>
    <a style="left:657px">WIR ÜBER UNS</a>
    <a style="left:755px">REFERENZEN</a>
    <a style="left:842px">AKTUELLES</a>
    <a class="active" style="left:921px">KONTAKT</a>
  </nav>
</header>

<div class="map" role="img" aria-label="Straßenkarte der Region mit Markierung des Firmenstandorts"></div>

<div class="crumbs">FALKE MONTAGEARBEITEN <span>»</span><span class="current">Kontakt</span></div>

<h1 class="page-title">Kontakt</h1>
<h2 class="page-sub">Immer für Sie da</h2>
<p class="intro">Unser erfahrenes Team ist vom Erstkontakt bis zur Realisierung Ihres Projektes und darüber hinaus immer für Sie da. Ob per E-Mail, telefo-nisch oder auch persönlich vor Ort –&nbsp; wir unterstützen Sie optimal bei der Umsetzung Ihres Vorhabens.</p>

<section class="contact-band">
</section>
<div class="callout">
  <p>Für sämtliche Anliegen oder Fragen in Zusammenhang mit unseren Dienstleistungen stehen wir Ihnen jederzeit gerne zur Verfügung. Wir freuen uns auf Ihren Anruf.</p>
  <div class="phone">
    <svg width="22" height="22" viewBox="0 0 24 24" aria-hidden="true"><path fill="#fff" d="M6.6 10.8c1.4 2.8 3.8 5.1 6.6 6.6l2.2-2.2c.3-.3.7-.4 1-.2 1.1.4 2.3.6 3.6.6.6 0 1 .4 1 1V20c0 .6-.4 1-1 1C10.6 21 3 13.4 3 4c0-.6.4-1 1-1h3.5c.6 0 1 .4 1 1 0 1.3.2 2.5.6 3.6.1.3 0 .7-.2 1L6.6 10.8z"/></svg>
    <span>+49 7000-481526</span>
  </div>
</div>
<h2 class="form-title">Kontaktformular</h2>
<address class="address">Falke Montagearbeiten<br>Lindenweg 12<br>70999 Talbach<br>Telefon: 07000-481526<br>Telefax: 07000-481527<br>E-Mail: info@falke-montage.de</address>
<div class="field name">Name *</div>
<div class="field mail">E-Mail-Adresse *</div>
<div class="field tel">Telefonnummer *</div>
<div class="field msg">Ihre Nachricht an uns</div>
<div class="submit">absenden</div>

<footer class="footer">FALKE MONTAGEARBEITEN   |  © 2017   |   IMPRESSUM</footer>
</body>
</html>
```